deceased estate cleaning services and cosmetic renovating

house frontage signage design
cur flute sign will be 600mm x 450 mm and no larger
is to be mounted of fence out front of projects as advertizing

Target Market(s)

elderly people and there sibling that need help

Colors
cadf82
85cae6
fbed22
85acd3
ffcf3e

Requirements
Must have
• clear phone number, email and business Name and logo
Should not have
• to much info and NO dark colors

```html
<!DOCTYPE html>
<html lang="en">
<head>
<meta charset="utf-8">
<title>TIDYHAVEN – Cosmetic Repairs &amp; House Maintenance</title>
<link rel="stylesheet" href="https://fonts.googleapis.com/css2?family=Bebas+Neue&family=Montserrat:wght@500;600;700;800;900&display=swap">
<style>
  :root {
    --grey-light: #efeff0;
    --grey-mid: #c9cacd;
    --green-dark: #5a9b48;
    --green-light: #8dc253;
    --green-title: #7aac3d;
    --green-shadow: #1f5a33;
    --red-dark: #a3232a;
    --red-light: #bd3036;
    --yellow: #f6ec3b;
    --ink: #2f2f2f;
    --white: #ffffff;
    --scene-cream: #f3e3bf;
    --scene-grey: #e4e5e7;
  }
  html, body {
    margin: 0;
    padding: 0;
    width: 1200px;
    height: 831px;
    overflow: hidden;
    background: var(--white);
  }
  .sign {
    display: block;
    width: 1200px;
    height: 831px;
  }
  .headline { font-family: "Bebas Neue", "Oswald", sans-serif; fill: var(--green-title); }
  .tagline { font-family: "Montserrat", Arial, sans-serif; font-weight: 700; fill: var(--ink); }
  .brand-name { font-family: "Montserrat", Arial, sans-serif; font-weight: 700; fill: var(--ink); }
  .slogan { font-family: "Montserrat", Arial, sans-serif; font-weight: 800; }
  .slogan-dark { fill: var(--ink); }
  .slogan-light { fill: var(--white); }
  .slogan-shadow { filter: drop-shadow(3px 3px 0 var(--green-shadow)); }
  .slogan-yellow { fill: var(--yellow); filter: drop-shadow(4px 4px 0 var(--green-shadow)); }
  .slogan-heavy { font-weight: 900; }
  .divider { stroke: var(--white); stroke-width: 2; opacity: .9; }
  .contact-lead { font-family: "Montserrat", Arial, sans-serif; font-weight: 600; fill: var(--white); }
  .contact-lead .accent { fill: var(--yellow); }
  .contact-phone { font-family: "Montserrat", Arial, sans-serif; font-weight: 800; fill: var(--white); }
  .contact-line { font-family: "Montserrat", Arial, sans-serif; font-weight: 700; fill: var(--white); }
  .icon { fill: none; stroke: var(--white); stroke-width: 2; stroke-linejoin: round; stroke-linecap: round; }
  .icon-solid { fill: var(--white); }
</style>
</head>
<body>
<svg class="sign" viewBox="0 0 1200 831" xmlns="http://www.w3.org/2000/svg">
  <defs>
    <linearGradient id="greyPanel" x1="0" y1="0" x2="1" y2="0">
      <stop offset="0" stop-color="var(--grey-mid)"/>
      <stop offset="0.55" stop-color="var(--grey-light)"/>
    </linearGradient>
    <linearGradient id="greenPanel" x1="0" y1="0" x2="1" y2="1">
      <stop offset="0" stop-color="var(--green-dark)"/>
      <stop offset="1" stop-color="var(--green-light)"/>
    </linearGradient>
    <linearGradient id="redBand" x1="0" y1="0" x2="1" y2="0">
      <stop offset="0" stop-color="var(--red-light)"/>
      <stop offset="1" stop-color="var(--red-dark)"/>
    </linearGradient>
    <linearGradient id="sceneTone" x1="0" y1="0" x2="1" y2="1">
      <stop offset="0" stop-color="var(--scene-cream)"/>
      <stop offset="0.6" stop-color="var(--scene-grey)"/>
      <stop offset="1" stop-color="#d9e4cc"/>
    </linearGradient>
  </defs>

  <!-- background panels -->
  <polygon class="panel-brand" points="0,0 343,0 456,150 352,296 0,296" fill="url(#greyPanel)"/>
  <polygon class="panel-slogan" points="0,296 352,296 612,686 505,686 443,831 0,831" fill="url(#greenPanel)"/>
  <polygon class="band-contact" points="505,686 1200,686 1200,831 443,831" fill="url(#redBand)"/>

  <!-- illustration area -->
  <rect class="scene" x="480" y="276" width="680" height="398" rx="6" fill="url(#sceneTone)"
        role="img" aria-label="Illustration: a house overflowing with household clutter being loaded onto a smiling driver's removal truck, with a recycling globe and city skyline behind"/>

  <!-- brand -->
  <text class="brand-name" x="195" y="238" font-size="50" text-anchor="middle" textLength="296" lengthAdjust="spacingAndGlyphs">TIDYHAVEN</text>

  <!-- headline -->
  <text class="headline" x="493" y="120" font-size="96" textLength="624" lengthAdjust="spacingAndGlyphs">COSMETIC REPAIRS &amp;</text>
  <text class="headline" x="493" y="199" font-size="96" textLength="628" lengthAdjust="spacingAndGlyphs">HOUSE MAINTENANCE</text>
  <text class="tagline" x="498" y="256" font-size="35" textLength="641" lengthAdjust="spacingAndGlyphs">QUALITY, PRIDE, PROFESSIONALISM</text>

  <!-- slogans -->
  <text class="slogan slogan-dark" x="60" y="378" font-size="46" textLength="286" lengthAdjust="spacingAndGlyphs">DE-CLUTTER</text>
  <text class="slogan slogan-light" x="59" y="435" font-size="58" textLength="298" lengthAdjust="spacingAndGlyphs">YOUR LIFE</text>
  <line class="divider" x1="42" y1="458" x2="420" y2="458"/>
  <text class="slogan slogan-light slogan-shadow" x="60" y="534" font-size="64" textLength="381" lengthAdjust="spacingAndGlyphs">WE’RE HERE</text>
  <text class="slogan slogan-yellow" x="57" y="615" font-size="89" textLength="389" lengthAdjust="spacingAndGlyphs">TO HELP</text>
  <line class="divider" x1="42" y1="651" x2="467" y2="651"/>
  <text class="slogan slogan-dark slogan-heavy" x="68" y="728" font-size="64" textLength="319" lengthAdjust="spacingAndGlyphs">RECYCLE</text>
  <text class="slogan slogan-light" x="68" y="789" font-size="58" textLength="254" lengthAdjust="spacingAndGlyphs">FOR LIFE</text>

  <!-- contact band -->
  <text class="contact-lead" x="534" y="734" font-size="28" textLength="646" lengthAdjust="spacingAndGlyphs">If you have any queries, <tspan class="accent">Get in touch</tspan> with us</text>

  <path class="icon-solid phone-icon" d="M514 768 q6 -5 11 0 l7 9 q3 5 -2 9 l-4 3 q4 10 14 16 l3 -4 q4 -5 9 -2 l9 6 q5 4 0 10 l-5 5 q-8 6 -22 -2 q-18 -12 -26 -30 q-6 -13 6 -20 z"/>
  <text class="contact-phone" x="568" y="802" font-size="53" textLength="316" lengthAdjust="spacingAndGlyphs">0400 555 218</text>

  <g class="icon email-icon">
    <rect x="905" y="762" width="21" height="16" rx="1.5"/>
    <polyline points="905,762 915.5,771 926,762"/>
  </g>
  <text class="contact-line" x="939" y="778" font-size="20" textLength="234" lengthAdjust="spacingAndGlyphs">info@tidyhaven.com.au</text>

  <g class="icon web-icon">
    <circle cx="915.5" cy="798" r="9.5"/>
    <ellipse cx="915.5" cy="798" rx="4" ry="9.5"/>
    <line x1="906" y1="798" x2="925" y2="798"/>
  </g>
  <text class="contact-line" x="939" y="807" font-size="20" textLength="234" lengthAdjust="spacingAndGlyphs">www.tidyhaven.com.au</text>
</svg>
</body>
</html>
```